Website for New Business in Luxury Home Market

Build a website for a new business that is an off shoot of my primary business as an interior designer. These days, with Nookly, KVBX and print media telling people they can be their own interior designer, General Contractors building a new home or remodeling, are frustrated because they do not get the information they need to be able to build or remodel. Clients/owners are often unaware that picking the pretty things like faucets, tile or appliances require specifications and drawings to tell the individual sub contractors how to proceed with their work, or to bid the project correctly. The professional interior designer used to fill this gap. Even if there is an architect on the project, many architects do not issue an ID Set (Interior Design Set). To fill this gap, we have started Tallow Design Group. Although we are interior designers, we will provide only specification services. By interfacing with the client and contractor, we will provide the client with a schedule and prompt them when it is time to shop. Additionally, we will give them a list of GC preferred vendors for them to shop with. Once selections have been made, specifications will be written, plans will be tagged. This process continues for all the pieces necessary for a home to be built: Plumbing, Appliances, Mouldings, Interior Doors, Cabinets, Hard Surfaces (Including counters, and showers), Flooring, Motorized Window Coverings, Hardware, Room Finish Schedule, Lighting - Recessed, Decorative and Exterior, Electrical Outlets, Exterior Hardscape Materials.

Professional contractors are used to receiving this information. Without the interior designer, the contractor often has to step in to guide the client. This takes him or her away from their actual job of building the house. What this translates to is a project that becomes late and over budget. The cost benefit of the specification process is that the project can be delivered on time, and helps to control the budget. By delivering on time, the homeowner does not incur additional interest charges and other costs involved in construction delays.

I would like a website that is built on a platform that I can edit if I need to do so, without having to call someone else to do it. Perhaps on Wix or Square Space if this is possible. I would like the ability to link social media. Also, if the photos need changing, it should be something simple for me to do. The website should be relatively simple. Show a few photos of the finished product along with the drawings that led up to them. I would also like to show a project spec sheet.

I've uploaded the photos and some of the documentation. The documentation will be a placeholder for the moment. I will change them to reflect the new logo and change the clients name. These will be ready next week, but for now we can use what I'm providing.

I like the "background' squiggle on my logo. Perhaps this can be integrated in some way. The website should tell in a concise manner what we do and who we do it for. It should appeal to the General Contractor, but could also be directed to the homeowner. I have lots of other photos if more are needed, but these are a start. I think too much info on the website won't help.

Target Market(s)

Luxury Home Builders; Professional General Contractors, People building luxury homes or remodeling a luxury property who don't want to use an interior designer.

Industry/Entity Type

Business

Coding

Coded - Design and coding required

Number of Pages Required

4 page

Other font styles liked:
• Use fonts that work with the logo I sent

Colors
ec1f27
c3c3c3

Requirements
Must have
• Company Name and Logo, About, Contact Us, FAQ, Photos and Specs. Use the files I sent for the Logo, and the colors for the website should be derived from those files. I like clean and simple.
Nice to have
• Builder Testimonials. I am working on getting two.
Should not have
• Not sure until I see it.

```html
<!DOCTYPE html>
<html lang="en">
<head>
<meta charset="utf-8">
<title>Tallow Design Group — Home Renovation</title>
<link rel="stylesheet" href="https://fonts.googleapis.com/css2?family=Poppins:wght@300;400;500;600&display=swap">
<style>
:root{
  --red:#ec1f27;
  --red-deep:#c8161d;
  --silver:#c3c3c3;
  --ink:#222222;
  --text:#3a3a3a;
  --muted:#777777;
  --topbar:#eeeeee;
  --soft:#f5f5f5;
  --footer:#262626;
  --footer-base:#1c1c1c;
  --white:#ffffff;
  --brand:#5a5a5a;
}
*{box-sizing:border-box;margin:0;padding:0}
html,body{width:1200px;height:3152px;overflow:hidden}
body{font-family:"Poppins",sans-serif;color:var(--text);background:var(--white);position:relative}

/* top bar */
.topbar{position:absolute;left:0;top:0;width:1200px;height:44px;background:var(--topbar);font-size:12px;color:var(--muted)}
.topbar .tagline{position:absolute;left:115px;top:13px}
.topbar .office{position:absolute;left:815px;top:12px;color:var(--ink);font-weight:500;font-size:13px;display:flex;align-items:center;gap:6px}
.social{display:flex;gap:14px;position:absolute}
.social span{width:12px;height:12px;border-radius:50%;background:var(--muted);display:block}
.topbar .social{left:1010px;top:16px}

/* header */
.header{position:absolute;left:0;top:44px;width:1200px;height:107px;background:var(--white)}
.brand{position:absolute;display:flex;align-items:center;gap:8px;font-weight:400;color:var(--brand);text-transform:uppercase;line-height:1.05}
.brand .mark{width:30px;height:30px;background:var(--red-deep);flex:none}
.header .brand{left:111px;top:32px;font-size:14px;width:130px}
.nav{position:absolute;left:504px;top:42px;font-size:14px;color:var(--ink)}
.nav a{color:inherit;text-decoration:none;position:absolute;white-space:nowrap}

/* hero */
.hero{position:absolute;left:0;top:151px;width:1200px;height:496px;background:linear-gradient(120deg,#2d2018 0%,#5a4331 40%,#3b2a1e 70%,#1f2a33 100%)}
.hero .shade{position:absolute;inset:0;background:rgba(0,0,0,.25)}
.hero h1{position:absolute;left:0;width:1200px;text-align:center;color:var(--white);font-weight:300;line-height:1}
.hero .l1{top:80px;font-size:76px}
.hero .l2{top:160px;font-size:80px;font-weight:400}
.hero p{position:absolute;left:0;top:260px;width:1200px;text-align:center;color:var(--white);font-size:22px;line-height:30px;font-weight:400}

/* section titles */
.title{position:absolute;left:0;width:1200px;text-align:center;font-size:42px;font-weight:300;color:var(--ink)}
.title b{font-weight:500}
.lead{position:absolute;text-align:center;font-size:12.5px;line-height:22px;color:var(--ink)}

/* services */
.services{position:absolute;left:0;top:647px;width:1200px;height:642px;background:var(--white)}
.service{position:absolute;width:310px;text-align:center}
.service svg{display:block;margin:0 auto;width:48px;height:48px}
.service h3{font-size:17px;font-weight:400;color:var(--ink);margin-top:8px}
.service p{font-size:12.5px;line-height:22px;color:var(--ink);margin-top:8px}

/* process */
.process{position:absolute;left:0;top:1292px;width:1200px;height:616px;background:var(--soft)}
.process h2{position:absolute;left:111px;top:80px;font-size:42px;font-weight:300;color:var(--ink)}
.process h2 b{font-weight:500}
.step{position:absolute;left:111px;width:400px;display:flex;gap:12px}
.step .thumb{width:88px;flex:none}
.step p{font-size:12.5px;line-height:22px;color:var(--ink)}
.process .photo{position:absolute;left:641px;top:0;width:559px;height:616px;background:linear-gradient(180deg,#1d2b4a 0%,#2c3550 35%,#6b5a45 70%,#2a2a22 100%)}
.sheet{position:absolute;left:544px;top:152px;width:318px;height:307px;background:var(--white);box-shadow:0 2px 10px rgba(0,0,0,.12)}
.sheet .drawing{position:absolute;left:22px;top:56px;width:274px;height:196px;background:linear-gradient(180deg,#f4f4f4,#e2e2e2)}
.sheet .notch{position:absolute;right:-12px;top:140px;width:0;height:0;border-top:12px solid transparent;border-bottom:12px solid transparent;border-left:12px solid var(--white)}

/* projects */
.projects{position:absolute;left:0;top:1908px;width:1200px;height:530px;background:var(--white)}
.grid{position:absolute;left:111px;top:147px;width:976px;height:362px;display:grid;grid-template-columns:repeat(4,244px);grid-template-rows:repeat(2,181px)}
.cell{position:relative;overflow:hidden}
.cell.red{background:var(--red);color:var(--white);text-align:center;padding:28px 22px 0}
.cell h4{font-size:17px;font-weight:400}
.cell p{font-size:12px;line-height:22px;margin-top:6px}
.cell.overlay{background:#4a0d0f;color:rgba(255,255,255,.28);text-align:center;padding:28px 22px 0}
.view{position:absolute;left:189px;top:73px;width:110px;height:38px;border:1px solid var(--white);color:var(--white);font-size:11px;display:flex;align-items:center;justify-content:center;letter-spacing:.5px;background:rgba(0,0,0,.35);z-index:2}

/* testimonial */
.testimonial{position:absolute;left:0;top:2438px;width:1200px;height:420px;background:#f7f7f7}
.avatar{position:absolute;left:527px;top:77px;width:148px;height:148px;border-radius:50%;background:radial-gradient(circle at 50% 40%,#d9b79c,#7a6252);border:5px solid var(--white)}
.testimonial p{position:absolute;left:180px;top:240px;width:840px;text-align:center;font-size:11.5px;line-height:22px;color:var(--muted)}
.dots{position:absolute;left:561px;top:345px;display:flex;gap:9px}
.dots span{width:12px;height:12px;border-radius:50%;background:#aaaaaa}
.dots span:first-child{background:var(--red)}

/* footer */
.footer{position:absolute;left:0;top:2858px;width:1200px;height:248px;background:var(--footer);color:var(--white)}
.footer .brand{left:111px;top:52px;font-size:14px;width:140px;color:#bdbdbd}
.footer .about{position:absolute;left:111px;top:134px;width:280px;font-size:12.5px;line-height:22px}
.footer h5{font-size:17px;font-weight:400;position:absolute}
.contact{position:absolute;left:467px;font-size:12.5px;line-height:22px}
.contact a{color:var(--red);text-decoration:none}
.contact b{font-weight:500}
.input{position:absolute;left:801px;top:78px;width:286px;height:42px;background:#3a3a3a;color:#9a9a9a;font-size:11px;padding:14px 12px}
.subscribe{position:absolute;left:801px;top:130px;width:120px;height:41px;background:var(--red);color:var(--white);font-size:12px;font-weight:500;display:flex;align-items:center;justify-content:center}
.basebar{position:absolute;left:0;top:3106px;width:1200px;height:46px;background:var(--footer-base);font-size:12px;color:#8a8a8a}
.basebar .social{left:111px;top:17px}
.basebar .social span{background:#8a8a8a}
.basebar .copy{position:absolute;right:111px;top:14px}
</style>
</head>
<body>

<div class="topbar">
  <span class="tagline">Hire us to turn your property around and make it stand out!</span>
  <span class="office">
    <svg width="12" height="12" viewBox="0 0 24 24"><path fill="#ec1f27" d="M6.6 10.8a15 15 0 006.6 6.6l2.2-2.2c.3-.3.7-.4 1-.2 1.1.4 2.3.6 3.6.6.6 0 1 .4 1 1V20c0 .6-.4 1-1 1A17 17 0 013 4c0-.6.4-1 1-1h3.5c.6 0 1 .4 1 1 0 1.3.2 2.5.6 3.6.1.3 0 .7-.2 1z"/></svg>
    Office: 555.214.3070
  </span>
  <div class="social"><span></span><span></span><span></span></div>
</div>

<header class="header">
  <div class="brand"><span class="mark"></span><span>Tallow Design Group</span></div>
  <nav class="nav">
    <a style="left:0">About</a>
    <a style="left:74px">Services</a>
    <a style="left:166px">Photos</a>
    <a style="left:248px">FAQ</a>
    <a style="left:311px">Specs</a>
    <a style="left:389px">Testimonials</a>
    <a style="left:507px">Contact us</a>
  </nav>
</header>

<section class="hero" role="img" aria-label="Photo of a renovated luxury kitchen with dark wood cabinetry, island and chandelier at dusk">
  <div class="shade"></div>
  <h1 class="l1">Home</h1>
  <h1 class="l2">Renovation</h1>
  <p>Sorem ipsum dolor sit amet, consectetuer adipiscing elit, sed diam<br>nonummy nibh euismod tincilaoreet<br>magna aliquamerat volutpat. Ut wisi enim ad minim.</p>
</section>

<section class="services">
  <h2 class="title" style="top:68px">Our <b>Services</b></h2>
  <p class="lead" style="left:111px;top:124px;width:976px">Sorem ipsum dolor sit amet, consectetuer adipiscing elit, sed diam nonummy nibh euismod tincilaoreet magna aliquamerat volutpat. Ut wisi enim ad minim. Sorem ipsum dolor sit amet, consectetuer adipiscing elit, sed diam nonummy nibh euismod tincilaoreet .</p>

  <div class="service" style="left:112px;top:192px">
    <svg viewBox="0 0 48 48" fill="none" stroke="#ec1f27" stroke-width="2"><path d="M6 22L24 8l18 14"/><rect x="10" y="20" width="28" height="22"/><rect x="15" y="26" width="7" height="6"/><rect x="26" y="26" width="7" height="6"/><path d="M10 35h28"/></svg>
    <h3>Home Remodeling</h3>
    <p>Sorem ipsum dolor sit amet, consectetu adipiscing elit, sed diam nonummy nibh euismod tincilaoreet magna aliquamerat volutpat. Ut wisi enim ad minim. Sorem ipsum dolor.</p>
  </div>
  <div class="service" style="left:446px;top:192px">
    <svg viewBox="0 0 48 48" fill="none" stroke="#ec1f27" stroke-width="2"><path d="M8 42V8l34 34z"/><path d="M15 35V25l10 10z"/><path d="M8 16h4M8 22h6M8 28h4"/></svg>
    <h3>New Home Construction</h3>
    <p>Sorem ipsum dolor sit amet, consectetu adipiscing elit, sed diam nonummy nibh euismod tincilaoreet magna aliquamerat volutpat. Ut wisi enim ad minim. Sorem ipsum dolor.</p>
  </div>
  <div class="service" style="left:778px;top:192px">
    <svg viewBox="0 0 48 48" fill="none" stroke="#ec1f27" stroke-width="2"><rect x="8" y="4" width="20" height="40"/><rect x="12" y="9" width="12" height="14"/><circle cx="24" cy="28" r="1.5"/><rect x="30" y="12" width="12" height="12"/><path d="M36 12v12M30 18h12"/></svg>
    <h3>Exterior Renovation</h3>
    <p>Sorem ipsum dolor sit amet, consectetu adipiscing elit, sed diam nonummy nibh euismod tincilaoreet magna aliquamerat volutpat. Ut wisi enim ad minim. Sorem ipsum dolor.</p>
  </div>
  <div class="service" style="left:112px;top:410px">
    <svg viewBox="0 0 48 48" fill="none" stroke="#ec1f27" stroke-width="2"><path d="M40 6L22 24"/><path d="M26 20l6 6-18 16H6v-8z"/><path d="M12 34l4 4M17 29l4 4"/></svg>
    <h3>Hardscapes</h3>
    <p>Sorem ipsum dolor sit amet, consectetu adipiscing elit, sed diam nonummy nibh euismod tincilaoreet magna aliquamerat volutpat. Ut wisi enim ad minim. Sorem ipsum dolor.</p>
  </div>
  <div class="service" style="left:446px;top:410px">
    <svg viewBox="0 0 48 48" fill="none" stroke="#ec1f27" stroke-width="2"><path d="M24 6v8M18 10h12"/><path d="M6 20h36c0 10-8 16-18 16S6 30 6 20z"/><path d="M20 36v6h8v-6"/></svg>
    <h3>Bathroom Remodeling</h3>
    <p>Sorem ipsum dolor sit amet, consectetu adipiscing elit, sed diam nonummy nibh euismod tincilaoreet magna aliquamerat volutpat. Ut wisi enim ad minim. Sorem ipsum dolor.</p>
  </div>
  <div class="service" style="left:778px;top:410px">
    <svg viewBox="0 0 48 48" fill="none" stroke="#ec1f27" stroke-width="2"><rect x="10" y="4" width="12" height="40" rx="2"/><path d="M22 12l10-4 6 14-16 18"/><path d="M13 10h6M13 18h6M13 26h6"/><circle cx="16" cy="38" r="2"/></svg>
    <h3>Kitchen Remodeling</h3>
    <p>Sorem ipsum dolor sit amet, consectetu adipiscing elit, sed diam nonummy nibh euismod tincilaoreet magna aliquamerat volutpat. Ut wisi enim ad minim. Sorem ipsum dolor.</p>
  </div>
</section>

<section class="process">
  <h2>Consecte <b>Adicing</b></h2>
  <div class="step" style="top:158px">
    <div class="thumb" role="img" aria-label="3D floor plan rendering" style="height:66px;background:linear-gradient(135deg,#e9e4dc,#b9a98f)"></div>
    <p>Sorem ipsum dolor sit amet,nsectetuer adipiscing elit, sed diam nonummy nibeuismod tincilaoreet magna aliquamerat volutpat. wisi enim ad minim. Sorem ipsum dolor sit amet,</p>
  </div>
  <div class="step" style="top:258px">
    <div class="thumb" role="img" aria-label="Interior elevation drawing" style="height:78px;background:linear-gradient(135deg,#f2f2f2,#cfcfcf)"></div>
    <p>Dorem ipsum dolor sit amet,nsectetuer adipiscing elit, sed diam nonummy nibeuismod tincilaoreet magna aliquamerat volutpat. wisi enim ad minim. Sorem ipsum dolor sit amet,</p>
  </div>
  <div class="step" style="top:368px">
    <div class="thumb" role="img" aria-label="Photo of a finished tiled shower" style="height:120px;background:linear-gradient(160deg,#d7cbbb,#7d6f60)"></div>
    <p>Worem ipsum dolor sit amet, consectetuer adipiscing elit, sed diam nonummy nibh euismod tincilaoreet magna aliquamerat volutpat. Ut wisi enim ad minim. Sorem ipsum dolor sit amet, consectetuer adipiscing elit, sed diam nonummy nibh euismod tincilaoreet .</p>
  </div>
  <div class="photo" role="img" aria-label="Photo of a luxury stone home exterior with arched window at dusk"></div>
  <div class="sheet">
    <div class="drawing" role="img" aria-label="Cabinet elevation drawing"></div>
    <div class="notch"></div>
  </div>
</section>

<section class="projects">
  <h2 class="title" style="top:48px">Our <b>Projects</b></h2>
  <p class="lead" style="left:0;top:100px;width:1200px">Sorem ipsum dolor sit amet, consectetuer adipiscing elit, sed diam nonummy nibh euismod tincilaoreet magna aliquamerat volutpat.</p>
  <div class="grid">
    <div class="cell" role="img" aria-label="Photo of a dark entry hall opening to a garden" style="background:linear-gradient(160deg,#1a1a1a,#3d3328);overflow:visible">
      <div class="view">VIEW DETAILS</div>
    </div>
    <div class="cell overlay"><h4>Project One</h4><p>Sorem ipsum dolor sit et, consectetu adipiscing elit, sed diam nonummy nibh euismod tincilaoreet.</p></div>
    <div class="cell" role="img" aria-label="Photo of a dining room with palm plant" style="background:linear-gradient(160deg,#3b3024,#8a7458)"></div>
    <div class="cell red"><h4>Project One</h4><p>Sorem ipsum dolor sit et, consectetu adipiscing elit, sed diam nonummy nibh euismod tincilaoreet.</p></div>
    <div class="cell red"><h4>Project One</h4><p>Sorem ipsum dolor sit et, consectetu adipiscing elit, sed diam nonummy nibh euismod tincilaoreet.</p></div>
    <div class="cell" role="img" aria-label="Photo of open doors onto a lawn and pool" style="background:linear-gradient(180deg,#4a3a28,#7b8a5a,#3a2e22)"></div>
    <div class="cell red"><h4>Project One</h4><p>Sorem ipsum dolor sit et, consectetu adipiscing elit, sed diam nonummy nibh euismod tincilaoreet.</p></div>
    <div class="cell" role="img" aria-label="Photo of a kitchen with island at night" style="background:linear-gradient(160deg,#2a2119,#6b5640,#1f2a3a)"></div>
  </div>
</section>

<section class="testimonial">
  <div class="avatar" role="img" aria-label="Portrait of the builder giving the testimonial"></div>
  <p>Contrary to popular belief, Lorem Ipsum is not simply random text. It has roots in a piece of classical Latin literature from 45 BC, making it over 2000 years old. Warren Ashby, a Latin professor at Fairmont Hill College in Virginia, looked up one of the. Contrary to popular belief, Lorem Ipsum is not simply random text. It has roots in a piece of classical Latin literature from 45 BC, making it over 2000 years old. Warren Ashby, a Latin professor at Fairmont Hill College in Virginia, looked up one of the.</p>
  <div class="dots"><span></span><span></span><span></span><span></span></div>
</section>

<footer class="footer">
  <div class="brand"><span class="mark" style="background:#8a8a8a"></span><span>Tallow Design Group</span></div>
  <p class="about">Sorem ipsum dolor sitconsectetuer adipiscing elit, sed diam nonu nibh euismod tincilaoreet magna aliquamerat volutpat. Ut wisi enim ad minim. .</p>

  <h5 style="left:467px;top:46px">Contacts</h5>
  <div class="contact" style="top:80px">
    48 Larkspur Row, Lorem Ipsum, CA 90000, USA<br>
    <a>info@tallowdesigngroup.com</a>
  </div>
  <h5 style="left:467px;top:138px">Call Us</h5>
  <div class="contact" style="top:172px">
    <b>Office: 555.214.3070</b><br>
    <b>Cell:&nbsp;&nbsp;&nbsp;&nbsp;&nbsp;555.214.3091</b>
  </div>

  <h5 style="left:801px;top:46px">Newsletter</h5>
  <div class="input">Enter your email</div>
  <div class="subscribe">SUBSCRIBE</div>
</footer>

<div class="basebar">
  <div class="social"><span></span><span></span><span></span></div>
  <span class="copy">copyrights © All Rights Reserved 2017</span>
</div>

</body>
</html>
```